Package for my report covers: Tavish Report Covers - 11x17

Packaging design single color will be screen printed on corrugated package. I will send photos of product as well as all the key features. Want a modern/corporate design that sells the product. Same packaging will be use to sell the variety of colors, and panel materials available. Will use a small barcode label (i have) to distinguish the color/material. You can see this product on my ecommerce website at: https://www.plumbrake-shop.com/5263/ will send example of current packaging of another product

Package size will be
Inside Length: 18.625"
Inside Width: 11.625"
Inside Height: 1.25"

Target Market(s)

Engineers, CAD Drafters, Business Professionals

Industry/Entity Type

Business Management

Font styles to use
Sans Serif

Colors
0455a3

Requirements
Must have
• Single Color Design, area for barcode
Nice to have
• lost of empty area (not overwhelming)
Should not have
• Profanities, sex,

```html
<!DOCTYPE html>
<html lang="en">
<head>
<meta charset="utf-8">
<title>Tavish Report Covers – Package Front</title>
<link rel="stylesheet" href="https://fonts.googleapis.com/css2?family=Montserrat:wght@400;600&display=swap">
<style>
  :root {
    --ink-blue: #0455a3;
    --board: #ffffff;
    --stage: #dcdcde;
  }
  * { margin: 0; padding: 0; box-sizing: border-box; }
  html, body {
    width: 1200px;
    height: 960px;
    overflow: hidden;
    background: var(--stage);
    font-family: "Montserrat", sans-serif;
  }
  .package-front {
    position: absolute;
    left: 290px;
    top: 40px;
    width: 620px;
    height: 880px;
    background: var(--board);
    overflow: hidden;
  }
  .brand-block {
    position: absolute;
    top: 70px;
    left: 0;
    width: 100%;
    text-align: center;
    color: var(--ink-blue);
  }
  .brand-ring {
    display: block;
    margin: 0 auto 24px;
    width: 124px;
    height: 124px;
    border: 13px solid var(--ink-blue);
    border-radius: 50%;
  }
  .brand-name {
    font-weight: 600;
    font-size: 60px;
    letter-spacing: 6px;
    line-height: 1;
  }
  .brand-product {
    margin-top: 8px;
    font-weight: 400;
    font-size: 28px;
    letter-spacing: 2px;
  }
  .blue-panel {
    position: absolute;
    top: 370px;
    left: 0;
    width: 100%;
    height: 510px;
    background: var(--ink-blue);
    border-top-right-radius: 60px;
  }
  .web-address {
    position: absolute;
    top: 34px;
    left: 0;
    width: 100%;
    text-align: center;
    color: var(--board);
    font-weight: 600;
    font-size: 13px;
    letter-spacing: 6px;
  }
  .monogram-area {
    position: absolute;
    left: 40px;
    top: 150px;
    width: 560px;
    height: 250px;
    background: var(--ink-blue);
    border: 3px solid var(--board);
    border-radius: 125px 0 0 125px;
    border-right: none;
  }
  .edition-year {
    position: absolute;
    left: 120px;
    top: 245px;
    color: var(--board);
    font-weight: 400;
    font-size: 44px;
    letter-spacing: 1px;
  }
  .barcode-area {
    position: absolute;
    right: 36px;
    bottom: 30px;
    width: 150px;
    height: 70px;
    background: var(--board);
  }
</style>
</head>
<body>
  <main class="package-front">
    <header class="brand-block">
      <span class="brand-ring"></span>
      <h1 class="brand-name">TAVISH</h1>
      <p class="brand-product">REPORT COVERS</p>
    </header>

    <section class="blue-panel">
      <p class="web-address">WWW.TAVISHCOVERS.COM</p>
      <div class="monogram-area" role="img" aria-label="Large flowing brand monogram lettering in single-colour knockout"></div>
      <p class="edition-year">2018</p>
      <div class="barcode-area" role="img" aria-label="Blank space for barcode label"></div>
    </section>
  </main>
</body>
</html>
```